Professional Lawn Treatment flyer (double sided) needed for established gardening company

We are an established and trusted gardening company in Swindon, UK, and are about to launch a new Lawn Treatment Service. This will be marketed to both existing and new customers and needs to reflect our current professional image. The flyer will need to be double-sided, portrait orientation and correctly sized so to be printed on A5.

If you look on our website www.tavistrowgardening.co.uk, you will see our colours are purple and green. We would like you to use these exact shades of purple and green in your design.

As part of the design, we will need you to put together an infographic table to show our packages. I have attached a spreadsheet which explains these packages but I will need you to create a visually appealing table that fits in with the overall design of the flyer. I don't want you to simply cut and paste my basic table into the design.

In terms of what needs to be included, I have tried to be as specific as possible here but please feel free to message me if you need any further information or clarification.

FRONT SIDE:
The title of our service is:
Expert Lawn Treatment Service

Our strapline will need to be included somewhere:
"Lawn care by your local gardening expert"

The front side of the flyer will need to contain our logo - different versions of which can be found within my dropbox folder here...

https://www.sharebinnu.co.uk/sh/k7qd21mzplax/QRT8xWbnNeLu4Pa-ZxYyhKcLo?dl=0

The front side will need to contain a main image (although feel free to add more if you have anything suitable). I have included a picture in the dropbox folder titled "Front side image" which we would like used. I've also included in the folder an adobe image of grass which you may or may not like to use on either front or back.

Somewhere on both the front and back sides, you will need to include our contact details:
01632 960417
www.tavistrowgardening.co.uk/lawncare

The front side should show what treatments we currently have available. These are:

- Lawn Fertilising
- Scarification
- Aeration
- Weed Control
- Moss Control
- Hydration Booster
- PlumeRest
- Turfing & Renovation

"Select a one-off treatment or choose from one of our specially created lawn care packages."

BACK SIDE:
On the back, we will still need our logo and contact details but the image we'd like used should be the one in the dropbox folder titled "Back side image". Again, if you have any other images you feel would also work, then please feel free to add them.

The back side is to contain a bit more information and be a bit 'wordier' and so can you please include the following 2 paragraphs:

"As expert gardeners, we are passionate about horticulture and working to bring out the very best in your garden. When we work in your garden, we look at it and treat it with the same care and attention as if it were our own, before handing it back for you to enjoy. Our passion doesn't end at just trees and shrubs though. Your grass is as much of a living, breathing plant as your shrubs and we therefore utilise our expert horticultural knowledge to ensure your lawn thrives and reaches its fullest potential.

Lawn care isn't just about applying a fertiliser. It's about really understanding your lawn and being able to use extensive knowledge and experience to diagnose and treat issues. It therefore stands to reason that you should employ an expert to bring out the best in your lawn which is why we at Tavistrow Gardening Services have created a superior lawn care service that will keep your lawn looking lush, green and healthy all year round."

I referred at the very top of this brief to the fact we will need an infographic table created to show the different lawn care packages available. You see from the PDF table I created that we have 3 packages; Standard, Enhanced and Premium. Please create a visually appealing table which sets out the differences between our packages and include it on the back page.

Finally, somewhere we would like reference to the other gardening services we do. It's only to be something small as it isn't the main focus of the flyer but we think it would be good to mention what else we do. To re-iterate, it isnt to be big. I still want the main focus to be lawn care but if you could somehow reference that we also do the following services, that would be good. I will leave it to you to decide where on the flyer it fits in best, be it the front or back:

- Lawn mowing
- Shrub pruning
- Hedge trimming
- Weed killing
- Garden clearance & tidy-up
- Planting & design
- Regular Garden Maintenance
- Turfing
- Fencing
- Gutter clearance

I think thats it. I look forward to your designs!
Ps. Don't forget the dropbox folder:

Target Market(s)

Professional men/women aged 25+
Retired aged 65+

Industry/Entity Type

Home And Garden

Font styles to use
Sans Serif

Colors
6b449b
9bcb3c

Requirements
Must have
• Our company colours; purple and green; as per our website www.tavistrowgardening.co.uk. I've selected purple and green on this brief just to highlight the colours needed but please be sure to use the exact shades from our website and NOT the shade of purple and green that were selected on this brief.
• All the wording as explained in the main project brief.
Nice to have
• I want the flyer to be bold, eye-catching and modern.
• We particularly like the font Trebuchet MS for general copy but please feel free to use any other font for bolder, main titles.
Should not have
• We don't want anything gimmicky. No cheesy marketing.
• We only want professional looking designs. With the greatest of respect, if you're just starting out or don't really do design but think you'll use this as practise, please don't waste your or our time. We've previously run contests for other projects where we've had designs submitted that have clearly been done on MS Word and used Clipart and Wordart. That's really not what we are looking for.

```html
<!DOCTYPE html>
<html lang="en">
<head>
<meta charset="utf-8">
<title>Tavistrow Gardening Services – Lawn Treatment Flyer</title>
<link href="https://fonts.googleapis.com/css2?family=Montserrat:wght@600;700;800&family=Fira+Sans:wght@400;500&family=Roboto+Condensed:wght@400;500&display=swap" rel="stylesheet">
<style>
:root{
  --purple:#6b449b;
  --purple-deep:#3d2459;
  --green:#9bcb3c;
  --grass:#4da92f;
  --grass-deep:#2f7d22;
  --stone:#c9c3b8;
  --lime:#d4e02a;
  --mid-green:#9ccc3c;
  --rich-green:#3cb44a;
  --white:#ffffff;
  --ink:#2b2b2b;
  --page-bg:#f2f2f0;
}
*{margin:0;padding:0;box-sizing:border-box}
html,body{width:1200px;height:1200px;overflow:hidden;background:var(--page-bg)}
.canvas{position:relative;width:1200px;height:1200px}
.flyer{position:absolute;top:218px;width:540px;height:764px;overflow:hidden;box-shadow:0 6px 20px rgba(0,0,0,.25)}
.flyer--front{left:40px}
.flyer--back{left:620px}

/* front */
.front-photo{position:absolute;inset:0;
  background:linear-gradient(118deg,var(--grass) 0%,var(--grass) 30%,var(--stone) 31%,#b9b3a8 55%,var(--grass) 56%,var(--grass-deep) 100%)}
.front-haze{position:absolute;left:0;top:0;width:100%;height:280px;
  background:linear-gradient(180deg,rgba(240,244,236,.9) 0%,rgba(226,236,220,.82) 80%,rgba(226,236,220,0) 100%)}
.brand{position:absolute;display:flex;align-items:center;gap:10px}
.brand__dot{width:26px;height:26px;border-radius:50%;background:var(--green)}
.brand__name{font-family:"Montserrat",sans-serif;font-weight:700;color:var(--purple-deep);font-size:19px;line-height:1.1;width:170px}
.front-brand{left:50px;top:70px}
.front-title{position:absolute;left:48px;top:182px;font-family:"Montserrat",sans-serif;font-weight:800;
  font-variant:small-caps;font-size:27px;color:var(--purple);letter-spacing:0;white-space:nowrap}
.intro{position:absolute;left:58px;top:344px;width:440px;font-family:"Montserrat",sans-serif;font-weight:700;
  text-transform:uppercase;font-size:13px;color:var(--purple);line-height:1.3}
.treatments{position:absolute;left:62px;top:400px;list-style:none;font-family:"Roboto Condensed",sans-serif;
  font-weight:500;font-size:17px;color:var(--purple);line-height:25px}
.treatments li::before{content:"• "}
.strapline{position:absolute;right:40px;top:640px;font-family:"Montserrat",sans-serif;font-weight:700;
  font-style:italic;text-transform:uppercase;color:var(--white);font-size:15px;letter-spacing:.5px}
.contact{position:absolute;right:40px;text-align:right;font-family:"Fira Sans",sans-serif;font-weight:500;color:var(--white);font-size:15px;line-height:24px}
.front-contact{top:670px}

/* back */
.back-photo{position:absolute;inset:0;
  background:linear-gradient(180deg,#6b6a4a 0%,#5f7f3a 28%,var(--grass) 45%,var(--grass) 80%,#a9a89f 100%)}
.back-photo::after{content:"";position:absolute;right:0;bottom:0;width:190px;height:420px;
  background:linear-gradient(200deg,rgba(190,186,176,0) 0%,rgba(190,186,176,.85) 35%,#b7b2a7 100%)}
.package-panel{position:absolute;left:0;top:30px;width:336px;height:280px;background:rgba(61,36,89,.82)}
.package-title{position:absolute;left:24px;top:44px;font-family:"Montserrat",sans-serif;font-weight:800;
  font-variant:small-caps;font-size:19px;color:var(--white);letter-spacing:.3px;white-space:nowrap}
.package-grid{position:absolute;left:24px;top:82px;width:296px;border-collapse:collapse}
.package-grid td{font-family:"Montserrat",sans-serif;font-weight:600;font-variant:small-caps;color:var(--white);
  font-size:13px;height:26px;padding:0;white-space:nowrap}
.package-grid td.marks{width:60px;text-align:right}
.mark{display:inline-block;width:18px;height:18px;border-radius:50%;margin-left:-6px;vertical-align:middle}
.mark--std{background:var(--lime)}
.mark--enh{background:var(--mid-green)}
.mark--pre{background:var(--rich-green)}
.legend{position:absolute;right:22px;top:150px;width:170px;list-style:none}
.legend li{display:flex;align-items:center;justify-content:flex-end;gap:12px;height:50px;
  font-family:"Fira Sans",sans-serif;font-weight:500;color:var(--white);font-size:13px;white-space:nowrap}
.legend .mark{width:36px;height:36px;margin:0}
.body-copy{position:absolute;left:24px;top:326px;width:320px;font-family:"Fira Sans",sans-serif;
  font-size:11.5px;line-height:15px;color:var(--ink)}
.body-copy p+p{margin-top:9px}
.also{position:absolute;left:368px;top:330px;width:160px}
.also__title{font-family:"Montserrat",sans-serif;font-weight:600;font-size:21px;color:var(--purple);margin-bottom:6px;white-space:nowrap}
.also__list{list-style:none;font-family:"Roboto Condensed",sans-serif;font-size:12px;line-height:16px;color:var(--purple)}
.also__list li::before{content:"• "}
.back-grass{position:absolute;left:0;bottom:0;width:100%;height:70px;
  background:linear-gradient(180deg,rgba(77,169,47,0) 0%,var(--grass) 40%,var(--grass-deep) 100%)}
.back-brand{left:30px;top:612px}
.back-contact{top:690px}
</style>
</head>
<body>
<main class="canvas">

  <section class="flyer flyer--front" aria-label="Flyer front">
    <div class="front-photo" role="img" aria-label="Photo of a green lawn with a curving stone paving path through a garden"></div>
    <div class="front-haze" role="img" aria-label="Faded photo of a landscaped garden with trees and a seating area"></div>
    <div class="brand front-brand"><span class="brand__dot"></span><span class="brand__name">Tavistrow Gardening Services</span></div>
    <h1 class="front-title">Expert Lawn Treatment Service</h1>
    <p class="intro">Select a one-off treatment or choose from one of our specially created lawn care packages.</p>
    <ul class="treatments">
      <li>Lawn Fertilising</li>
      <li>Scarification</li>
      <li>Aeration</li>
      <li>Weed Control</li>
      <li>Moss Control</li>
      <li>Hydration Booster</li>
      <li>PlumeRest</li>
      <li>Turfing &amp; Renovation</li>
    </ul>
    <p class="strapline">Lawn care by your local gardening expert</p>
    <p class="contact front-contact">01632 960417<br>www.tavistrowgardening.co.uk/lawncare</p>
  </section>

  <section class="flyer flyer--back" aria-label="Flyer back">
    <div class="back-photo" role="img" aria-label="Photo of a striped lawn beside a log cabin deck with garden chairs and a block-paved path"></div>
    <div class="package-panel"></div>
    <h2 class="package-title">Lawn Treatment Packages</h2>
    <table class="package-grid">
      <tr><td>Spring Treatment</td><td class="marks"><span class="mark mark--std"></span><span class="mark mark--enh"></span><span class="mark mark--pre"></span></td></tr>
      <tr><td>Early Summer Treatment</td><td class="marks"><span class="mark mark--std"></span><span class="mark mark--enh"></span><span class="mark mark--pre"></span></td></tr>
      <tr><td>Late Summer Treatment</td><td class="marks"><span class="mark mark--std"></span><span class="mark mark--enh"></span><span class="mark mark--pre"></span></td></tr>
      <tr><td>Autumn/Winter Treatment</td><td class="marks"><span class="mark mark--std"></span><span class="mark mark--enh"></span><span class="mark mark--pre"></span></td></tr>
      <tr><td>Scarification</td><td class="marks"><span class="mark mark--std"></span><span class="mark mark--enh"></span><span class="mark mark--pre"></span></td></tr>
      <tr><td>Aeration</td><td class="marks"><span class="mark mark--enh"></span><span class="mark mark--pre"></span></td></tr>
      <tr><td>PlumeRest Treatment</td><td class="marks"><span class="mark mark--enh"></span><span class="mark mark--pre"></span></td></tr>
      <tr><td>Hydration Boost Treatment</td><td class="marks"><span class="mark mark--pre"></span></td></tr>
    </table>
    <ul class="legend">
      <li>Standard Package <span class="mark mark--std"></span></li>
      <li>Enhanced Package <span class="mark mark--enh"></span></li>
      <li>Premium Package <span class="mark mark--pre"></span></li>
    </ul>
    <div class="body-copy">
      <p>As expert gardeners, we are passionate about horticulture and working to bring out the very best in your garden. When we work in your garden, we look at it and treat it with the same care and attention as if it were our own, before handing it back for you to enjoy. Our passion doesn't end at just trees and shrubs though. Your grass is as much of a living, breathing plant as your shrubs and we therefore utilise our expert horticultural knowledge to ensure your lawn thrives and reaches its fullest potential.</p>
      <p>Lawn care isn't just about applying a fertiliser. It's about really understanding your lawn and being able to use extensive knowledge and experience to diagnose and treat issues. It therefore stands to reason that you should employ an expert to bring out the best in your lawn which is why we at Tavistrow Gardening Services have created a superior lawn care service that will keep your lawn looking lush, green and healthy all year round.</p>
    </div>
    <aside class="also">
      <h3 class="also__title">WE ALSO DO</h3>
      <ul class="also__list">
        <li>Lawn mowing</li>
        <li>Shrub pruning</li>
        <li>Hedge trimming</li>
        <li>Weed killing</li>
        <li>Garden clearance &amp; tidy-up</li>
        <li>Planting &amp; design</li>
        <li>Regular Garden Maintenance</li>
        <li>Turfing</li>
        <li>Fencing</li>
        <li>Gutter clearance</li>
      </ul>
    </aside>
    <div class="back-grass" role="img" aria-label="Close-up of grass blades along the bottom edge"></div>
    <div class="brand back-brand"><span class="brand__dot"></span><span class="brand__name">Tavistrow Gardening Services</span></div>
    <p class="contact back-contact">01632 960417<br>www.tavistrowgardening.co.uk/lawncare</p>
  </section>

</main>
</body>
</html>
```